QTVlink PowerPoint Template with existing Logo and Letterhead template

Develop a PowerPoint template based on existing logo and letterhead designs for a Marketing Consultancy.
Presentations that will be made with title slide, content slides (which includes mostly bullet point text and some tables) and also last page company introduction and copyright.
Corporate colors should be keep as per the logo

I like something like from Pixel Harbor
- Serious, Modern PowerPoint Design for Company in Canada | Design 418674
- Professional, Modern PowerPoint Design for Company in United States | Design 7795293
- Professional, Modern PowerPoint Design for Company in United States | Design 7826742
- Serious, Modern PowerPoint Design for Company in Canada | Design 418635
- Elegant, Serious PowerPoint Design for Company in Puerto Rico | Design 16951178
- Bold, Modern PowerPoint Design for Company in United States | Design 11745238

To all designers, • We need sleek and modern looking PowerPoint presentation template. • The template will primarily be used for our corporate slide and solutions presentation for our customers. • Not too much of white and it should be sleek, modern and impressive for marketing consultancy firms like us. • Please ensure the content pages are water marketed with the 4 boxes. • I like something like from Pixel Harbor and you can get some idea on what I like.: o Serious, Modern PowerPoint Design for Company in Canada | Design 418674 o Professional, Modern PowerPoint Design for Company in United States | Design 7795293 o Professional, Modern PowerPoint Design for Company in United States | Design 7826742 o Serious, Modern PowerPoint Design for Company in Canada | Design 418635 o Elegant, Serious PowerPoint Design for Company in Puerto Rico | Design 16951178 o Bold, Modern PowerPoint Design for Company in United States | Design 11745238 Thanks!

Target Market(s)

Marketing Managers, B2B Marketing Team, CRM Data Owners

Industry/Entity Type

Marketing

Requirements
Must have
• Not too much of white and it should be sleek, modern and impressive for marketing consultancy firms like us. Please ensure the content pages are water marketed with the 4 boxes. The template will primarily be used for our corporate slides and solutions presentation for our customers.
Should not have
• no background in the slide content area

```html
<!DOCTYPE html>
<html lang="en">
<head>
<meta charset="utf-8">
<title>QTVlink Presentation Template Overview</title>
<link href="https://fonts.googleapis.com/css2?family=Raleway:wght@400;600;700;800&family=Open+Sans:wght@400;600&display=swap" rel="stylesheet">
<style>
:root{
  --red:#e31f26;--red-d:#c8161d;--slate:#4b5263;--slate-d:#383e4c;--ink:#2b2f3a;
  --grey:#8a8f9b;--mid:#b9bdc6;--light:#eef0f3;--line:#dde0e5;--white:#fff;
}
*{box-sizing:border-box}
html,body{margin:0;width:1200px;height:3942px;overflow:hidden;background:#fff}
.deck{display:grid;grid-template-columns:repeat(3,1fr);grid-auto-rows:222px;gap:10px;padding:4px;width:1200px;height:3942px}
.slide{position:relative;overflow:hidden;background:var(--white);box-shadow:0 0 0 1px #e2e4e8;font-family:'Open Sans',sans-serif;color:var(--ink)}
.slide>*{position:absolute}
.hd{left:14px;top:9px;font:600 9.5px/1 'Raleway',sans-serif;color:var(--ink)}
.brand{font:800 9px/1 'Raleway',sans-serif;color:var(--red);letter-spacing:.6px;text-transform:uppercase;display:flex;align-items:center;gap:3px}
.brand::after{content:"";width:5px;height:5px;background:var(--red)}
.brand.top{right:12px;top:8px}
.brand.lg{font-size:20px;gap:6px}.brand.lg::after{width:10px;height:10px}
.foot{left:0;right:0;bottom:0;height:11px;border-top:1px solid var(--line);font-size:3.6px;color:var(--grey);padding-left:10px;line-height:10px}
.ph{background:linear-gradient(160deg,#c9d2dc,#7f8ea0 55%,#4f5a68)}
.ph.dark{background:linear-gradient(160deg,#5b6474,#2e3340)}
.ph.warm{background:linear-gradient(160deg,#f0b46a,#a4663a 50%,#3c3a42)}
.ph.light{background:linear-gradient(160deg,#f4f5f7,#c7ccd4)}
.ph.blue{background:linear-gradient(160deg,#3a5a85,#14223a)}
.p{font-size:4.5px;line-height:6.5px;color:var(--grey)}
.p.w{color:#f3f4f6}
.h{font:700 6px/1.2 'Raleway',sans-serif;color:var(--ink)}
.h.red{color:var(--red)}.h.w{color:#fff}
.big{font:600 17px/1.1 'Raleway',sans-serif;color:#fff}
.red-bg{background:var(--red)}.slate-bg{background:var(--slate)}.dark-bg{background:var(--slate-d)}.light-bg{background:var(--light)}
.num{width:12px;height:12px;background:var(--red);color:#fff;font:700 6px/12px 'Raleway',sans-serif;text-align:center}
.dot{width:5px;height:5px;border-radius:50%;background:var(--red)}
.ico{width:12px;height:12px;border-radius:50%;background:var(--red)}
.ico.s{background:var(--slate)}
.pct{font:700 14px/1 'Raleway',sans-serif;color:var(--ink)}
.badge{width:46px;height:22px;border:1px solid var(--mid);border-radius:3px}
.badge.c{border-radius:50%;width:26px;height:26px}
</style>
</head>
<body>
<main class="deck">

<!-- 1 cover -->
<section class="slide">
  <div class="ph" role="img" aria-label="Glass skyscrapers seen from below" style="left:0;top:0;right:0;height:150px"></div>
  <div class="big" style="left:18px;top:40px">Your Title Goes Here</div>
  <div class="p w" style="left:18px;top:62px;font-size:6px">Your Subtitle Goes Here</div>
  <div class="p w" style="left:18px;top:128px">www.qtvlink.com</div>
  <div class="brand lg" style="left:96px;top:172px">QTVlink</div>
</section>

<!-- 2 -->
<section class="slide" style="background:linear-gradient(90deg,#f7f8fa,#e9ebef)">
  <div class="big" style="left:18px;top:40px;color:var(--ink)"><span style="color:var(--red)">Your</span> Title Here</div>
  <div class="p" style="left:18px;top:62px;font-size:6px">Your Subtitle Goes Here</div>
  <div class="red-bg" style="left:250px;top:14px;width:34px;height:34px"></div>
  <div class="red-bg" style="left:292px;top:100px;width:60px;height:60px"></div>
  <div style="left:300px;top:40px;width:26px;height:26px;background:#d3d6dc"></div>
</section>

<!-- 3 -->
<section class="slide red-bg">
  <div class="big" style="left:18px;top:40px">Your <span style="opacity:.7">Title Here</span></div>
  <div class="p w" style="left:18px;top:62px;font-size:6px">Your Subtitle Goes Here</div>
  <div class="ph dark" role="img" aria-label="Dark architectural detail" style="left:270px;top:14px;width:36px;height:36px"></div>
  <div class="ph dark" role="img" aria-label="Dark office interior" style="left:300px;top:90px;width:64px;height:64px"></div>
</section>

<!-- 4 -->
<section class="slide">
  <div class="ph dark" role="img" aria-label="Office towers in slate tone" style="inset:0"></div>
  <div class="brand lg" style="left:130px;top:70px">QTVlink</div>
  <div class="big" style="left:80px;top:102px;font-weight:400">Your Title Goes Here</div>
  <div class="p w" style="left:150px;top:124px">Your Subtitle Goes Here</div>
</section>

<!-- 5 agenda -->
<section class="slide">
  <div class="hd">Our Agenda</div><div class="brand top">QTVlink</div>
  <div class="num" style="left:20px;top:52px">01</div><div class="h" style="left:38px;top:52px">Agenda Title</div><div class="p" style="left:38px;top:60px;width:80px">Short agenda note here</div>
  <div class="num" style="left:20px;top:92px">02</div><div class="h" style="left:38px;top:92px">Agenda Title</div><div class="p" style="left:38px;top:100px;width:80px">Short agenda note here</div>
  <div class="num" style="left:20px;top:132px">03</div><div class="h" style="left:38px;top:132px">Agenda Title</div><div class="p" style="left:38px;top:140px;width:80px">Short agenda note here</div>
  <div class="num" style="left:200px;top:52px">04</div><div class="h" style="left:218px;top:52px">Agenda Title</div><div class="p" style="left:218px;top:60px;width:80px">Short agenda note here</div>
  <div class="num" style="left:200px;top:92px">05</div><div class="h" style="left:218px;top:92px">Agenda Title</div><div class="p" style="left:218px;top:100px;width:80px">Short agenda note here</div>
  <div class="num" style="left:200px;top:132px">06</div><div class="h" style="left:218px;top:132px">Agenda Title</div><div class="p" style="left:218px;top:140px;width:80px">Short agenda note here</div>
  <div class="foot">© Copyright QTVlink. All rights reserved.</div>
</section>

<!-- 6 market overview -->
<section class="slide">
  <div class="hd">Market Overview</div><div class="brand top">QTVlink</div>
  <div class="h" style="left:14px;top:38px">Heading Text</div>
  <div class="p" style="left:14px;top:48px;width:90px">Lorem ipsum dolor sit amet, consectetur adipiscing elit sed do eiusmod tempor.</div>
  <div class="ph" role="img" aria-label="City towers" style="left:112px;top:32px;width:140px;height:80px"></div>
  <svg style="left:275px;top:32px" width="80" height="80" viewBox="0 0 80 80"><circle cx="40" cy="40" r="30" fill="none" stroke="#e3e5e9" stroke-width="8"/><circle cx="40" cy="40" r="30" fill="none" stroke="#e31f26" stroke-width="8" stroke-dasharray="113 189" transform="rotate(-90 40 40)"/><text x="40" y="44" font-family="Raleway" font-weight="700" font-size="12" text-anchor="middle" fill="#2b2f3a">60%</text></svg>
  <div class="h red" style="left:112px;top:124px">Heading Text</div>
  <div class="p" style="left:112px;top:134px;width:140px">Lorem ipsum dolor sit amet, consectetur adipiscing elit sed do eiusmod tempor incididunt ut labore.</div>
  <div class="p" style="left:275px;top:124px;width:100px">Lorem ipsum dolor sit amet, consectetur adipiscing elit sed do.</div>
  <div class="foot">© Copyright QTVlink. All rights reserved.</div>
</section>

<!-- 7 bullets -->
<section class="slide">
  <div class="hd">Bullets Point 1 Level</div><div class="brand top">QTVlink</div>
  <div class="dot" style="left:16px;top:52px"></div><div class="h" style="left:26px;top:51px">Your Text Here</div><div class="p" style="left:26px;top:60px;width:90px">Lorem ipsum dolor sit amet, consectetur elit.</div>
  <div class="dot" style="left:140px;top:52px"></div><div class="h" style="left:150px;top:51px">Your Text Here</div><div class="p" style="left:150px;top:60px;width:90px">Lorem ipsum dolor sit amet, consectetur elit.</div>
  <div class="dot" style="left:264px;top:52px"></div><div class="h" style="left:274px;top:51px">Your Text Here</div><div class="p" style="left:274px;top:60px;width:90px">Lorem ipsum dolor sit amet, consectetur elit.</div>
  <div class="dot" style="left:16px;top:122px"></div><div class="h" style="left:26px;top:121px">Your Text Here</div><div class="p" style="left:26px;top:130px;width:90px">Lorem ipsum dolor sit amet, consectetur elit.</div>
  <div class="dot" style="left:140px;top:122px"></div><div class="h" style="left:150px;top:121px">Your Text Here</div><div class="p" style="left:150px;top:130px;width:90px">Lorem ipsum dolor sit amet, consectetur elit.</div>
  <div class="dot" style="left:264px;top:122px"></div><div class="h" style="left:274px;top:121px">Your Text Here</div><div class="p" style="left:274px;top:130px;width:90px">Lorem ipsum dolor sit amet, consectetur elit.</div>
  <div class="foot">© Copyright QTVlink. All rights reserved.</div>
</section>

<!-- 8 -->
<section class="slide">
  <div class="ph" role="img" aria-label="Glass tower facade" style="left:0;top:0;width:130px;height:222px"></div>
  <div class="red-bg" style="left:130px;top:0;width:130px;height:111px"></div>
  <div class="h w" style="left:142px;top:18px">Heading Goes Here</div>
  <div class="p w" style="left:142px;top:30px;width:108px">Lorem ipsum dolor sit amet, consectetur adipiscing elit sed do eiusmod tempor incididunt.</div>
  <div class="ph" role="img" aria-label="Office building from below" style="left:260px;top:0;width:131px;height:111px"></div>
  <div class="ph dark" role="img" aria-label="Modern glass architecture" style="left:130px;top:111px;width:130px;height:111px"></div>
  <div class="slate-bg" style="left:260px;top:111px;width:131px;height:111px"></div>
  <div class="h w" style="left:272px;top:128px">Heading Goes Here</div>
  <div class="p w" style="left:272px;top:140px;width:108px">Lorem ipsum dolor sit amet, consectetur adipiscing elit sed do eiusmod tempor incididunt.</div>
</section>

<!-- 9 -->
<section class="slide">
  <div class="hd">Your Title Here</div><div class="brand top">QTVlink</div>
  <div style="left:0;top:30px;width:98px;height:150px;background:#fff"></div>
  <div class="red-bg" style="left:98px;top:30px;width:98px;height:150px"></div>
  <div class="dark-bg" style="left:196px;top:30px;width:97px;height:150px"></div>
  <div style="left:293px;top:30px;width:98px;height:150px;background:#7a808e"></div>
  <div class="ico" style="left:43px;top:50px;background:none;border:1px solid var(--slate)"></div>
  <div class="ico" style="left:141px;top:50px;background:none;border:1px solid #fff"></div>
  <div class="ico" style="left:239px;top:50px;background:none;border:1px solid #fff"></div>
  <div class="ico" style="left:336px;top:50px;background:none;border:1px solid #fff"></div>
  <div class="h" style="left:22px;top:76px">Heading Here</div><div class="p" style="left:12px;top:88px;width:76px;text-align:center">Lorem ipsum dolor sit amet consectetur elit sed.</div>
  <div class="h w" style="left:120px;top:76px">Heading Here</div><div class="p w" style="left:110px;top:88px;width:76px;text-align:center">Lorem ipsum dolor sit amet consectetur elit sed.</div>
  <div class="h w" style="left:218px;top:76px">Heading Here</div><div class="p w" style="left:208px;top:88px;width:76px;text-align:center">Lorem ipsum dolor sit amet consectetur elit sed.</div>
  <div class="h w" style="left:315px;top:76px">Heading Here</div><div class="p w" style="left:305px;top:88px;width:76px;text-align:center">Lorem ipsum dolor sit amet consectetur elit sed.</div>
  <div class="foot">© Copyright QTVlink. All rights reserved.</div>
</section>

<!-- 10 differences -->
<section class="slide">
  <div class="hd">Our Differences</div><div class="brand top">QTVlink</div>
  <div class="slate-bg" style="left:0;top:44px;right:0;height:120px"></div>
  <div class="dot" style="left:22px;top:62px"></div><div class="p w" style="left:32px;top:60px;width:170px">Lorem ipsum dolor sit amet, consectetur adipiscing elit.</div>
  <div class="dot" style="left:22px;top:86px"></div><div class="p w" style="left:32px;top:84px;width:170px">Lorem ipsum dolor sit amet, consectetur adipiscing elit.</div>
  <div class="dot" style="left:22px;top:110px"></div><div class="p w" style="left:32px;top:108px;width:170px">Lorem ipsum dolor sit amet, consectetur adipiscing elit.</div>
  <div class="dot" style="left:22px;top:134px"></div><div class="p w" style="left:32px;top:132px;width:170px">Lorem ipsum dolor sit amet, consectetur adipiscing elit.</div>
  <div class="ph" role="img" aria-label="Skyscrapers converging upward" style="left:230px;top:30px;width:140px;height:148px"></div>
  <div class="foot">© Copyright QTVlink. All rights reserved.</div>
</section>

<!-- 11 text & bullet -->
<section class="slide">
  <div class="hd">Text &amp; Bullet Area</div><div class="brand top">QTVlink</div>
  <div class="h red" style="left:14px;top:40px">Heading Goes Here</div>
  <div class="p" style="left:14px;top:52px;width:110px">Lorem ipsum dolor sit amet, consectetur adipiscing elit sed do eiusmod tempor incididunt ut labore et dolore magna aliqua.</div>
  <div class="ico" style="left:150px;top:40px"></div><div class="h" style="left:168px;top:43px">Your Text Here</div>
  <div class="ico s" style="left:150px;top:66px"></div><div class="h" style="left:168px;top:69px">Your Text Here</div>
  <div class="ico" style="left:150px;top:92px"></div><div class="h" style="left:168px;top:95px">Your Text Here</div>
  <div class="ico s" style="left:150px;top:118px"></div><div class="h" style="left:168px;top:121px">Your Text Here</div>
  <div class="ico s" style="left:265px;top:40px"></div><div class="h" style="left:283px;top:43px">Your Text Here</div>
  <div class="ico" style="left:265px;top:66px"></div><div class="h" style="left:283px;top:69px">Your Text Here</div>
  <div class="ico s" style="left:265px;top:92px"></div><div class="h" style="left:283px;top:95px">Your Text Here</div>
  <div class="ico" style="left:265px;top:118px"></div><div class="h" style="left:283px;top:121px">Your Text Here</div>
  <div class="foot">© Copyright QTVlink. All rights reserved.</div>
</section>

<!-- 12 clients -->
<section class="slide">
  <div class="badge" style="left:20px;top:24px"></div><div class="badge c" style="left:150px;top:20px"></div><div class="badge" style="left:270px;top:24px"></div><div class="badge c" style="left:340px;top:20px"></div>
  <div class="badge c" style="left:30px;top:92px"></div><div class="badge" style="left:310px;top:94px"></div>
  <div class="red-bg" style="left:110px;top:76px;width:170px;height:56px"></div>
  <div class="h w" style="left:110px;top:97px;width:170px;text-align:center;font-size:11px;font-weight:600">Our Awesome Client</div>
  <div class="badge" style="left:20px;top:164px"></div><div class="badge c" style="left:110px;top:160px"></div><div class="badge" style="left:200px;top:164px"></div><div class="badge" style="left:300px;top:164px"></div>
</section>

<!-- 13 five columns -->
<section class="slide">
  <div style="left:0;top:0;width:79px;height:222px;background:#6e7482"></div>
  <div style="left:78px;top:0;width:79px;height:222px;background:#7c8290"></div>
  <div style="left:156px;top:0;width:79px;height:222px;background:#8a909d"></div>
  <div style="left:234px;top:0;width:79px;height:222px;background:#9aa0ac"></div>
  <div class="red-bg" style="left:312px;top:0;width:79px;height:222px"></div>
  <div class="ico" style="left:33px;top:60px;background:none;border:1px solid #fff"></div>
  <div class="ico" style="left:111px;top:60px;background:none;border:1px solid #fff"></div>
  <div class="ico" style="left:189px;top:60px;background:none;border:1px solid #fff"></div>
  <div class="ico" style="left:267px;top:60px;background:none;border:1px solid #fff"></div>
  <div class="ico" style="left:345px;top:60px;background:none;border:1px solid #fff"></div>
  <div class="h w" style="left:14px;top:96px">Heading Here</div><div class="p w" style="left:10px;top:108px;width:60px">Lorem ipsum dolor sit amet elit.</div>
  <div class="h w" style="left:92px;top:96px">Heading Here</div><div class="p w" style="left:88px;top:108px;width:60px">Lorem ipsum dolor sit amet elit.</div>
  <div class="h w" style="left:170px;top:96px">Heading Here</div><div class="p w" style="left:166px;top:108px;width:60px">Lorem ipsum dolor sit amet elit.</div>
  <div class="h w" style="left:248px;top:96px">Heading Here</div><div class="p w" style="left:244px;top:108px;width:60px">Lorem ipsum dolor sit amet elit.</div>
  <div class="h w" style="left:326px;top:96px">Heading Here</div><div class="p w" style="left:322px;top:108px;width:60px">Lorem ipsum dolor sit amet elit.</div>
</section>

<!-- 14 mockup -->
<section class="slide">
  <div class="hd">Our Mockup Area</div><div class="brand top">QTVlink</div>
  <div class="slate-bg" style="left:0;top:120px;right:0;height:102px"></div>
  <div class="ph light" role="img" aria-label="Laptop screen showing a slide" style="left:110px;top:40px;width:170px;height:110px;border:5px solid #2b2f3a"></div>
  <div class="brand" style="left:160px;top:88px;font-size:12px">QTVlink</div>
  <div class="h" style="left:14px;top:50px">Heading Here</div><div class="p" style="left:14px;top:60px;width:80px">Lorem ipsum dolor sit amet elit.</div>
  <div class="h" style="left:300px;top:50px">Heading Here</div><div class="p" style="left:300px;top:60px;width:80px">Lorem ipsum dolor sit amet elit.</div>
  <div class="h w" style="left:14px;top:160px">Heading Here</div><div class="p w" style="left:14px;top:170px;width:80px">Lorem ipsum dolor sit amet elit.</div>
  <div class="h w" style="left:300px;top:160px">Heading Here</div><div class="p w" style="left:300px;top:170px;width:80px">Lorem ipsum dolor sit amet elit.</div>
</section>

<!-- 15 picture slide -->
<section class="slide">
  <div class="slate-bg" style="left:0;top:0;width:160px;height:222px"></div>
  <div class="ph dark" role="img" aria-label="Circular office photo" style="left:40px;top:70px;width:80px;height:80px;border-radius:50%;border:3px solid var(--red)"></div>
  <div class="h w" style="left:40px;top:104px;width:80px;text-align:center">PICTURE SLIDE</div>
  <svg style="left:190px;top:40px" width="180" height="100" viewBox="0 0 180 100"><g fill="#e31f26"><rect x="0" y="40" width="14" height="60"/><rect x="40" y="20" width="14" height="80"/><rect x="80" y="50" width="14" height="50"/><rect x="120" y="10" width="14" height="90"/></g><g fill="#4b5263"><rect x="16" y="60" width="14" height="40"/><rect x="56" y="45" width="14" height="55"/><rect x="96" y="30" width="14" height="70"/><rect x="136" y="55" width="14" height="45"/></g></svg>
  <svg style="left:190px;top:156px" width="10" height="10"><path d="M5 1 9 9H1z" fill="#e31f26"/></svg>
  <div class="pct" style="left:204px;top:154px">85%</div>
  <div class="p" style="left:190px;top:172px;width:170px">Lorem ipsum dolor sit amet, consectetur adipiscing elit sed do.</div>
</section>

<!-- 16 mockup red -->
<section class="slide">
  <div class="red-bg" style="left:0;top:0;width:150px;height:222px"></div>
  <div class="hd" style="color:#fff">Our Mockup Area</div><div class="brand top">QTVlink</div>
  <div class="h w" style="left:14px;top:44px">Heading Here</div>
  <div class="p w" style="left:14px;top:56px;width:120px">Lorem ipsum dolor sit amet, consectetur adipiscing elit sed do eiusmod.</div>
  <div class="ph light" role="img" aria-label="Desktop monitor showing a slide" style="left:170px;top:30px;width:190px;height:120px;border:5px solid #2b2f3a"></div>
  <div class="brand" style="left:225px;top:84px;font-size:14px">QTVlink</div>
  <div class="ico s" style="left:14px;top:120px"></div><div class="p" style="left:30px;top:122px;color:#fff">Your text here</div>
  <div class="ico s" style="left:14px;top:142px"></div><div class="p" style="left:30px;top:144px;color:#fff">Your text here</div>
  <div class="foot">© Copyright QTVlink. All rights reserved.</div>
</section>

<!-- 17 line chart -->
<section class="slide">
  <div class="brand top">QTVlink</div>
  <div class="h" style="left:14px;top:30px;font-size:10px;font-weight:600">This Is Line<br>Chart Slide</div>
  <div class="red-bg p w" style="left:14px;top:58px;padding:1px 6px">Creative Text Here</div>
  <div class="p" style="left:14px;top:74px;width:100px">Lorem ipsum dolor sit amet, consectetur adipiscing elit sed do.</div>
  <svg style="left:150px;top:30px" width="220" height="130" viewBox="0 0 220 130"><g stroke="#e3e5e9"><line x1="0" y1="20" x2="220" y2="20"/><line x1="0" y1="60" x2="220" y2="60"/><line x1="0" y1="100" x2="220" y2="100"/></g><polyline points="0,90 50,40 100,95 150,30 210,70" fill="none" stroke="#e31f26" stroke-width="2"/><polyline points="0,60 50,80 100,50 150,85 210,60" fill="none" stroke="#4b5263" stroke-width="1.5"/></svg>
  <div class="foot">© Copyright QTVlink. All rights reserved.</div>
</section>

<!-- 18 -->
<section class="slide">
  <div class="hd">Your Title Goes Here</div><div class="brand top">QTVlink</div>
  <div class="ph" role="img" aria-label="Tower photo" style="left:14px;top:30px;width:120px;height:70px"></div>
  <div class="red-bg" style="left:14px;top:104px;width:120px;height:70px"></div><div class="h w" style="left:24px;top:132px">Heading Goes Here</div>
  <div class="slate-bg" style="left:140px;top:30px;width:120px;height:70px"></div><div class="h w" style="left:150px;top:58px">Heading Goes Here</div>
  <div class="ph dark" role="img" aria-label="Glass building" style="left:140px;top:104px;width:120px;height:70px"></div>
  <div class="ph" role="img" aria-label="High-rise detail" style="left:266px;top:30px;width:112px;height:70px"></div>
  <div class="slate-bg" style="left:266px;top:104px;width:112px;height:70px"></div><div class="h w" style="left:276px;top:132px">Heading Goes Here</div>
  <div class="foot">© Copyright QTVlink. All rights reserved.</div>
</section>

<!-- 19 about -->
<section class="slide">
  <div class="ph light" role="img" aria-label="Bright office corridor" style="left:0;top:0;width:230px;height:222px"></div>
  <div class="red-bg" style="left:180px;top:40px;width:180px;height:120px"></div>
  <div class="h w" style="left:196px;top:60px;font-size:9px">About Us</div>
  <div class="p w" style="left:196px;top:76px;width:150px">Lorem ipsum dolor sit amet, consectetur adipiscing elit sed do eiusmod tempor incididunt ut labore et dolore.</div>
</section>

<!-- 20 divider -->
<section class="slide">
  <div class="ph dark" role="img" aria-label="Slate-toned city skyline" style="inset:0"></div>
  <div class="big" style="left:30px;top:96px;font-size:15px"><span style="color:var(--red)">Title Here</span> Divider Page</div>
</section>

<!-- 21 quote -->
<section class="slide">
  <div class="hd">Quote Area</div><div class="brand top">QTVlink</div>
  <div class="ph warm" role="img" aria-label="City skyline at sunset" style="left:150px;top:28px;width:241px;height:180px"></div>
  <div class="slate-bg" style="left:0;top:28px;width:150px;height:180px"></div>
  <div class="p w" style="left:14px;top:60px;width:124px;font-size:6px;line-height:9px">“Coming together is a beginning; keeping together is progress; working together is success.”</div>
  <div class="p w" style="left:14px;top:104px">- Avery Lund</div>
</section>

<!-- 22 brand detailed -->
<section class="slide">
  <div class="hd">Brand Detailed</div><div class="brand top">QTVlink</div>
  <div class="ph light" role="img" aria-label="Laptop on a desk" style="left:14px;top:34px;width:160px;height:140px"></div>
  <div class="red-bg" style="left:180px;top:34px;width:95px;height:68px"></div><div class="h w" style="left:188px;top:44px">Strategy</div><div class="p w" style="left:188px;top:54px;width:80px">Lorem ipsum dolor sit amet elit.</div>
  <div class="slate-bg" style="left:278px;top:34px;width:95px;height:68px"></div><div class="h w" style="left:286px;top:44px">Technology</div><div class="p w" style="left:286px;top:54px;width:80px">Lorem ipsum dolor sit amet elit.</div>
  <div class="dark-bg" style="left:180px;top:106px;width:95px;height:68px"></div><div class="h w" style="left:188px;top:116px">Research</div><div class="p w" style="left:188px;top:126px;width:80px">Lorem ipsum dolor sit amet elit.</div>
  <div class="light-bg" style="left:278px;top:106px;width:95px;height:68px"></div><div class="h" style="left:286px;top:116px">Digital</div><div class="p" style="left:286px;top:126px;width:80px">Lorem ipsum dolor sit amet elit.</div>
  <div class="foot">© Copyright QTVlink. All rights reserved.</div>
</section>

<!-- 23 product philosophy -->
<section class="slide">
  <div class="hd">Product Philosophy</div><div class="brand top">QTVlink</div>
  <svg style="left:150px;top:50px" width="90" height="90" viewBox="0 0 90 90"><circle cx="45" cy="45" r="32" fill="none" stroke="#4b5263" stroke-width="18"/><circle cx="45" cy="45" r="32" fill="none" stroke="#e31f26" stroke-width="18" stroke-dasharray="120 201" transform="rotate(-90 45 45)"/></svg>
  <div class="ico s" style="left:120px;top:38px"></div><div class="h" style="left:40px;top:40px;width:76px;text-align:right">Visual</div><div class="p" style="left:40px;top:50px;width:76px;text-align:right">Lorem ipsum dolor sit.</div>
  <div class="ico s" style="left:120px;top:140px"></div><div class="h" style="left:40px;top:142px;width:76px;text-align:right">Word Process</div><div class="p" style="left:40px;top:152px;width:76px;text-align:right">Lorem ipsum dolor sit.</div>
  <div class="ico s" style="left:258px;top:38px"></div><div class="h" style="left:276px;top:40px">Web Upgrade</div><div class="p" style="left:276px;top:50px;width:76px">Lorem ipsum dolor sit.</div>
  <div class="ico s" style="left:258px;top:140px"></div><div class="h" style="left:276px;top:142px">Fabrication</div><div class="p" style="left:276px;top:152px;width:76px">Lorem ipsum dolor sit.</div>
  <div class="foot">© Copyright QTVlink. All rights reserved.</div>
</section>

<!-- 24 bar chart city -->
<section class="slide">
  <div class="ph light" role="img" aria-label="Faded city skyline" style="left:0;top:0;right:0;height:110px"></div>
  <svg style="left:20px;top:40px" width="350" height="120" viewBox="0 0 350 120"><g fill="#e31f26"><rect x="10" y="40" width="22" height="80"/><rect x="100" y="10" width="22" height="110"/><rect x="190" y="50" width="22" height="70"/><rect x="280" y="30" width="22" height="90"/></g><g fill="#4b5263"><rect x="34" y="60" width="22" height="60"/><rect x="124" y="50" width="22" height="70"/><rect x="214" y="70" width="22" height="50"/><rect x="304" y="60" width="22" height="60"/></g></svg>
  <div class="h" style="left:36px;top:166px">Asia</div><div class="h" style="left:122px;top:166px">Africa</div><div class="h" style="left:208px;top:166px">America</div><div class="h" style="left:300px;top:166px">Europe</div>
  <div class="p" style="left:24px;top:176px;width:70px">Lorem ipsum dolor.</div><div class="p" style="left:112px;top:176px;width:70px">Lorem ipsum dolor.</div><div class="p" style="left:200px;top:176px;width:70px">Lorem ipsum dolor.</div><div class="p" style="left:290px;top:176px;width:70px">Lorem ipsum dolor.</div>
  <div class="foot">© Copyright QTVlink. All rights reserved.</div>
</section>

<!-- 25 trending -->
<section class="slide">
  <div class="hd">Trending In The World</div><div class="brand top">QTVlink</div>
  <div class="ph light" role="img" aria-label="World map" style="left:14px;top:40px;width:220px;height:120px;border-radius:6px"></div>
  <div class="red-bg" style="left:70px;top:76px;width:36px;height:36px;border-radius:50%;color:#fff;font:700 9px/36px Raleway,sans-serif;text-align:center">80%</div>
  <div class="slate-bg" style="left:160px;top:84px;width:36px;height:36px;border-radius:50%;color:#fff;font:700 9px/36px Raleway,sans-serif;text-align:center">75%</div>
  <div class="ico" style="left:250px;top:48px"></div><div class="h" style="left:268px;top:48px">Consulting</div><div class="p" style="left:268px;top:57px;width:100px">Lorem ipsum dolor sit amet.</div>
  <div class="ico s" style="left:250px;top:84px"></div><div class="h" style="left:268px;top:84px">Strategy</div><div class="p" style="left:268px;top:93px;width:100px">Lorem ipsum dolor sit amet.</div>
  <div class="ico" style="left:250px;top:120px"></div><div class="h" style="left:268px;top:120px">Performance</div><div class="p" style="left:268px;top:129px;width:100px">Lorem ipsum dolor sit amet.</div>
  <div class="foot">© Copyright QTVlink. All rights reserved.</div>
</section>

<!-- 26 vision mission -->
<section class="slide">
  <div class="hd">Our Vision &amp; Mission</div><div class="brand top">QTVlink</div>
  <div class="ph dark" role="img" aria-label="Slate-toned office scene" style="left:0;top:28px;right:0;height:160px"></div>
  <div class="ico" style="left:20px;top:44px"></div><div class="h w" style="left:36px;top:47px;font-size:8px">Our Vision</div>
  <div class="h w" style="left:20px;top:66px">Go to the Next Level</div>
  <div class="p w" style="left:20px;top:76px;width:150px">Lorem ipsum dolor sit amet, consectetur adipiscing elit sed do eiusmod tempor incididunt.</div>
  <div class="ico" style="left:210px;top:44px"></div><div class="h w" style="left:226px;top:47px;font-size:8px">Our Missions</div>
  <div class="p w" style="left:220px;top:66px">› Your Text Here</div><div class="p w" style="left:220px;top:78px">› Your Text Here</div><div class="p w" style="left:220px;top:90px">› Your Text Here</div><div class="p w" style="left:220px;top:102px">› Your Text Here</div>
  <div class="foot">© Copyright QTVlink. All rights reserved.</div>
</section>

<!-- 27 services -->
<section class="slide">
  <div class="hd">Our Services</div><div class="brand top">QTVlink</div>
  <div class="ph blue" role="img" aria-label="Digital circuit network" style="left:14px;top:34px;width:180px;height:140px"></div>
  <div class="red-bg" style="left:14px;top:140px;width:180px;height:34px"></div>
  <div class="h w" style="left:24px;top:146px">Your Title Goes Here</div><div class="p w" style="left:24px;top:156px;width:160px">Lorem ipsum dolor sit amet, consectetur.</div>
  <div class="ico" style="left:210px;top:44px"></div><div class="h red" style="left:228px;top:44px">Service Number One</div><div class="p" style="left:228px;top:53px;width:140px">Lorem ipsum dolor sit amet elit.</div>
  <div class="ico s" style="left:210px;top:84px"></div><div class="h red" style="left:228px;top:84px">Service Number Two</div><div class="p" style="left:228px;top:93px;width:140px">Lorem ipsum dolor sit amet elit.</div>
  <div class="ico" style="left:210px;top:124px"></div><div class="h red" style="left:228px;top:124px">Service Number Three</div><div class="p" style="left:228px;top:133px;width:140px">Lorem ipsum dolor sit amet elit.</div>
  <div class="foot">© Copyright QTVlink. All rights reserved.</div>
</section>

<!-- 28 three column -->
<section class="slide">
  <div class="hd">Three Column Description</div><div class="brand top">QTVlink</div>
  <div class="h red" style="left:14px;top:36px;width:330px;font-size:7px">This is place for your header text. Insert your text here, just replace the text with your own text.</div>
  <div class="p" style="left:14px;top:64px;width:110px">Lorem ipsum dolor sit amet, consectetur adipiscing elit sed do eiusmod tempor incididunt ut labore et dolore magna aliqua ut enim.</div>
  <div class="p" style="left:138px;top:64px;width:110px">Lorem ipsum dolor sit amet, consectetur adipiscing elit sed do eiusmod tempor incididunt ut labore et dolore magna aliqua ut enim.</div>
  <div class="p" style="left:262px;top:64px;width:110px">Lorem ipsum dolor sit amet, consectetur adipiscing elit sed do eiusmod tempor incididunt ut labore et dolore magna aliqua ut enim.</div>
  <div class="foot">© Copyright QTVlink. All rights reserved.</div>
</section>

<!-- 29 team single -->
<section class="slide">
  <div class="hd">Our Team</div><div class="brand top">QTVlink</div>
  <div class="ph light" role="img" aria-label="Team member portrait" style="left:70px;top:40px;width:60px;height:60px;border-radius:50%"></div>
  <div class="p" style="left:150px;top:50px;width:200px">Lorem ipsum dolor sit amet, consectetur adipiscing elit sed do eiusmod tempor incididunt ut labore.</div>
  <div class="h" style="left:60px;top:110px;width:80px;text-align:center">Rhea Solen</div><div class="p" style="left:60px;top:120px;width:80px;text-align:center">Designer</div>
  <div class="h red" style="left:60px;top:132px;width:80px;text-align:center;letter-spacing:2px">★★★★★</div>
  <div class="foot">© Copyright QTVlink. All rights reserved.</div>
</section>

<!-- 30 subscription -->
<section class="slide">
  <div class="hd">Monthly Subscription</div><div class="brand top">QTVlink</div>
  <div class="slate-bg" style="left:0;top:30px;right:0;height:140px"></div>
  <div class="dark-bg" style="left:40px;top:50px;width:96px;height:22px;color:#fff;font:700 10px/22px Raleway,sans-serif;text-align:center">$300</div>
  <div style="left:40px;top:72px;width:96px;height:84px;background:#fff"></div>
  <div class="red-bg" style="left:146px;top:38px;width:100px;height:28px;color:#fff;font:700 13px/28px Raleway,sans-serif;text-align:center">$900</div>
  <div style="left:146px;top:66px;width:100px;height:98px;background:#fff"></div>
  <div class="dark-bg" style="left:256px;top:50px;width:96px;height:22px;color:#fff;font:700 10px/22px Raleway,sans-serif;text-align:center">$400</div>
  <div style="left:256px;top:72px;width:96px;height:84px;background:#fff"></div>
  <div class="p" style="left:50px;top:82px;line-height:10px">Feature one<br>Feature two<br>Feature three<br>Feature four</div>
  <div class="p" style="left:158px;top:78px;line-height:11px">Feature one<br>Feature two<br>Feature three<br>Feature four</div>
  <div class="p" style="left:266px;top:82px;line-height:10px">Feature one<br>Feature two<br>Feature three<br>Feature four</div>
  <div class="foot">© Copyright QTVlink. All rights reserved.</div>
</section>

<!-- 31 table -->
<section class="slide">
  <div class="hd">Your Title Goes Here</div><div class="brand top">QTVlink</div>
  <svg style="left:14px;top:34px" width="210" height="140" viewBox="0 0 210 140"><rect width="210" height="14" fill="#4b5263"/><g fill="#eef0f3"><rect y="28" width="210" height="14"/><rect y="56" width="210" height="14"/><rect y="84" width="210" height="14"/><rect y="112" width="210" height="14"/></g><g font-family="Open Sans" font-size="5" fill="#fff"><text x="6" y="9">Item</text><text x="60" y="9">Q1</text><text x="100" y="9">Q2</text><text x="140" y="9">Q3</text><text x="180" y="9">Q4</text></g><g font-family="Open Sans" font-size="5" fill="#8a8f9b"><text x="6" y="23">Lorem</text><text x="6" y="37">Ipsum</text><text x="6" y="51">Dolor</text><text x="6" y="65">Amet</text><text x="6" y="79">Elit</text><text x="6" y="93">Sed</text><text x="6" y="107">Tempor</text><text x="6" y="121">Magna</text><text x="6" y="135">Aliqua</text><text x="60" y="23">24</text><text x="100" y="23">31</text><text x="140" y="23">18</text><text x="180" y="23">40</text><text x="60" y="51">12</text><text x="100" y="51">27</text><text x="140" y="51">35</text><text x="180" y="51">22</text><text x="60" y="79">30</text><text x="100" y="79">16</text><text x="140" y="79">29</text><text x="180" y="79">33</text><text x="60" y="107">19</text><text x="100" y="107">25</text><text x="140" y="107">41</text><text x="180" y="107">28</text></g></svg>
  <div class="p" style="left:240px;top:40px;width:130px">Lorem ipsum dolor sit amet, consectetur adipiscing elit sed do eiusmod tempor incididunt ut labore et dolore magna aliqua.</div>
  <div class="foot">© Copyright QTVlink. All rights reserved.</div>
</section>

<!-- 32 team four -->
<section class="slide">
  <div class="hd">Our Team</div><div class="brand top">QTVlink</div>
  <div class="ph light" role="img" aria-label="Team member portrait" style="left:20px;top:40px;width:28px;height:28px;border-radius:50%"></div><div class="h" style="left:56px;top:42px">Noel Brandt</div><div class="p" style="left:56px;top:52px;width:100px">Lorem ipsum dolor sit amet elit.</div>
  <div class="ph light" role="img" aria-label="Team member portrait" style="left:200px;top:40px;width:28px;height:28px;border-radius:50%"></div><div class="h" style="left:236px;top:42px">Orin Kell</div><div class="p" style="left:236px;top:52px;width:100px">Lorem ipsum dolor sit amet elit.</div>
  <div class="ph light" role="img" aria-label="Team member portrait" style="left:20px;top:100px;width:28px;height:28px;border-radius:50%"></div><div class="h" style="left:56px;top:102px">Tessa Vane</div><div class="p" style="left:56px;top:112px;width:100px">Lorem ipsum dolor sit amet elit.</div>
  <div class="ph light" role="img" aria-label="Team member portrait" style="left:200px;top:100px;width:28px;height:28px;border-radius:50%"></div><div class="h" style="left:236px;top:102px">Lena Morrow</div><div class="p" style="left:236px;top:112px;width:100px">Lorem ipsum dolor sit amet elit.</div>
  <div class="foot">© Copyright QTVlink. All rights reserved.</div>
</section>

<!-- 33 testimonials -->
<section class="slide">
  <div class="hd">Customer Testimonials</div><div class="brand top">QTVlink</div>
  <div class="ph light" role="img" aria-label="Customer portrait" style="left:30px;top:36px;width:30px;height:30px;border-radius:50%"></div>
  <div class="p" style="left:72px;top:40px;width:290px">“Lorem ipsum dolor sit amet, consectetur adipiscing elit sed do eiusmod tempor incididunt ut labore.”</div>
  <div class="slate-bg" style="left:0;top:110px;right:0;height:80px"></div>
  <div class="ico s" style="left:60px;top:126px;background:none;border:1px solid #fff;width:20px;height:20px"></div>
  <div class="ico s" style="left:150px;top:126px;background:none;border:1px solid #fff;width:20px;height:20px"></div>
  <div class="ico s" style="left:240px;top:126px;background:none;border:1px solid #fff;width:20px;height:20px"></div>
  <div class="ico s" style="left:320px;top:126px;background:none;border:1px solid #fff;width:20px;height:20px"></div>
  <div class="p w" style="left:50px;top:154px;width:40px;text-align:center">Your text</div><div class="p w" style="left:140px;top:154px;width:40px;text-align:center">Your text</div><div class="p w" style="left:230px;top:154px;width:40px;text-align:center">Your text</div><div class="p w" style="left:310px;top:154px;width:40px;text-align:center">Your text</div>
  <div class="foot">© Copyright QTVlink. All rights reserved.</div>
</section>

<!-- 34 two pictures -->
<section class="slide">
  <div class="hd">Two Pictures Slide</div>
  <div class="ph blue" role="img" aria-label="City towers at night" style="left:14px;top:34px;width:176px;height:150px"></div>
  <div class="ph" role="img" aria-label="Skyscraper facade" style="left:200px;top:34px;width:176px;height:150px"></div>
  <div class="foot">© Copyright QTVlink. All rights reserved.</div>
</section>

<!-- 35 title image text -->
<section class="slide">
  <div class="hd">Title And Image + Text</div><div class="brand top">QTVlink</div>
  <div class="ph light" role="img" aria-label="Modern office hall" style="left:14px;top:28px;width:362px;height:100px"></div>
  <div class="h red" style="left:14px;top:140px;width:180px;font-size:7px;font-weight:600">Lorem ipsum dolor sit amet, consectetur adipiscing elit sed do eiusmod.</div>
  <div class="p" style="left:210px;top:140px;width:166px">Lorem ipsum dolor sit amet, consectetur adipiscing elit sed do eiusmod tempor incididunt ut labore et dolore.</div>
  <div class="foot">© Copyright QTVlink. All rights reserved.</div>
</section>

<!-- 36 sales comparison -->
<section class="slide">
  <div class="hd">Sales Comparison</div><div class="brand top">QTVlink</div>
  <div class="h red" style="left:60px;top:38px">Red Sales</div><div class="h" style="left:290px;top:38px">Grey Sales</div>
  <svg style="left:20px;top:50px" width="120" height="80" viewBox="0 0 120 80"><g fill="#e31f26"><rect x="0" y="30" width="12" height="50"/><rect x="22" y="10" width="12" height="70"/><rect x="44" y="40" width="12" height="40"/><rect x="66" y="20" width="12" height="60"/><rect x="88" y="0" width="12" height="80"/></g></svg>
  <svg style="left:250px;top:50px" width="120" height="80" viewBox="0 0 120 80"><g fill="#4b5263"><rect x="0" y="40" width="12" height="40"/><rect x="22" y="20" width="12" height="60"/><rect x="44" y="10" width="12" height="70"/><rect x="66" y="35" width="12" height="45"/><rect x="88" y="15" width="12" height="65"/></g></svg>
  <svg style="left:178px;top:80px" width="34" height="20" viewBox="0 0 34 20"><circle cx="10" cy="10" r="8" fill="none" stroke="#4b5263" stroke-width="3"/><circle cx="24" cy="10" r="8" fill="none" stroke="#4b5263" stroke-width="3"/></svg>
  <div class="pct" style="left:20px;top:144px;color:var(--red)">45%</div><div class="p" style="left:58px;top:146px;width:80px">Lorem ipsum dolor sit.</div>
  <div class="pct" style="left:250px;top:144px">68%</div><div class="p" style="left:288px;top:146px;width:80px">Lorem ipsum dolor sit.</div>
  <div class="foot">© Copyright QTVlink. All rights reserved.</div>
</section>

<!-- 37 -->
<section class="slide">
  <div class="ph" role="img" aria-label="Office skyline" style="inset:0"></div>
  <div class="h w" style="left:100px;top:20px;font-size:9px">Your Title Goes Here</div>
  <div class="red-bg" style="left:0;top:100px;width:140px;height:122px"></div>
  <div class="p w" style="left:12px;top:112px;width:116px">Lorem ipsum dolor sit amet, consectetur adipiscing elit sed do eiusmod tempor incididunt.</div>
  <div class="slate-bg" style="left:140px;top:100px;width:125px;height:122px"></div>
  <div class="p w" style="left:152px;top:112px;width:100px">Lorem ipsum dolor sit amet, consectetur adipiscing elit sed do.</div>
  <div style="left:265px;top:100px;width:126px;height:122px;background:#7a808e"></div>
  <div class="p w" style="left:277px;top:112px;width:100px">Lorem ipsum dolor sit amet, consectetur adipiscing elit sed do.</div>
</section>

<!-- 38 timeline page -->
<section class="slide">
  <div class="brand lg" style="left:140px;top:40px">QTVlink</div>
  <div class="h" style="left:145px;top:66px;width:100px;text-align:center;font-size:8px;font-weight:600">Timeline Page</div>
  <div class="slate-bg" style="left:0;top:100px;right:0;height:122px"></div>
  <div class="h red" style="left:145px;top:108px;width:100px;text-align:center">Your Heading Here</div>
  <div style="left:194px;top:120px;width:2px;height:102px;background:var(--red)"></div>
  <div class="p w" style="left:40px;top:130px;width:140px;text-align:right">Lorem ipsum dolor sit amet, consectetur adipiscing elit sed do.</div>
</section>

<!-- 39 your title -->
<section class="slide">
  <div class="hd">Your Title</div><div class="brand top">QTVlink</div>
  <div class="ph" role="img" aria-label="Towers against blue sky" style="left:200px;top:0;width:191px;height:120px"></div>
  <div class="dot" style="left:16px;top:40px"></div><div class="h red" style="left:26px;top:39px">Bullet Point</div>
  <div class="p" style="left:26px;top:50px;width:150px">Lorem ipsum dolor sit amet, consectetur adipiscing elit sed do.</div>
  <div class="slate-bg" style="left:0;top:120px;right:0;height:88px"></div>
  <div class="p w" style="left:16px;top:136px;width:160px">Lorem ipsum dolor sit amet, consectetur adipiscing elit sed do eiusmod tempor.</div>
  <div class="dot" style="left:260px;top:140px;background:#fff"></div><div class="p w" style="left:270px;top:138px">Bullet Point</div>
  <div class="foot">© Copyright QTVlink. All rights reserved.</div>
</section>

<!-- 40 your title -->
<section class="slide">
  <div class="hd">Your Title</div><div class="brand top">QTVlink</div>
  <div class="ph dark" role="img" aria-label="Dark glass tower" style="left:200px;top:28px;width:176px;height:100px"></div>
  <div class="red-bg" style="left:200px;top:128px;width:176px;height:60px"></div>
  <div class="p w" style="left:210px;top:138px;width:156px">Lorem ipsum dolor sit amet, consectetur adipiscing elit sed do eiusmod tempor.</div>
  <div class="dot" style="left:16px;top:42px"></div><div class="h red" style="left:26px;top:41px">Bullet Point</div><div class="p" style="left:26px;top:51px;width:150px">Lorem ipsum dolor sit amet elit.</div>
  <div class="dot" style="left:16px;top:92px;background:var(--slate)"></div><div class="h" style="left:26px;top:91px">Chart</div><div class="p" style="left:26px;top:101px;width:150px">Lorem ipsum dolor sit amet elit.</div>
  <div class="dot" style="left:16px;top:142px;background:var(--slate)"></div><div class="h" style="left:26px;top:141px">Share</div><div class="p" style="left:26px;top:151px;width:150px">Lorem ipsum dolor sit amet elit.</div>
  <div class="foot">© Copyright QTVlink. All rights reserved.</div>
</section>

<!-- 41 timeline -->
<section class="slide">
  <div style="left:90px;top:0;width:2px;height:222px;background:var(--red)"></div>
  <div class="dot" style="left:88px;top:30px;width:6px;height:6px"></div><div class="dot" style="left:88px;top:80px;width:6px;height:6px"></div><div class="dot" style="left:88px;top:130px;width:6px;height:6px"></div><div class="dot" style="left:88px;top:180px;width:6px;height:6px"></div>
  <div class="h red" style="left:30px;top:29px;width:50px;text-align:right">Your Title</div>
  <div class="p" style="left:104px;top:28px;width:200px">Lorem ipsum dolor sit amet, consectetur adipiscing elit sed do.</div>
  <div class="pct" style="left:104px;top:68px">85%</div>
  <div class="p" style="left:104px;top:86px;width:200px">Lorem ipsum dolor sit amet, consectetur adipiscing elit.</div>
  <div class="slate-bg" style="left:20px;top:128px;width:60px;height:30px"></div><div class="p w" style="left:26px;top:134px;width:50px">Lorem ipsum dolor sit.</div>
  <div class="h red" style="left:104px;top:178px">Your Title</div>
</section>

<!-- 42 who we are -->
<section class="slide">
  <div class="hd">Who We Are?</div><div class="brand top">QTVlink</div>
  <div class="dot" style="left:16px;top:42px"></div><div class="h" style="left:26px;top:40px;width:60px">A Title About Contents</div>
  <div class="dot" style="left:16px;top:92px"></div><div class="h" style="left:26px;top:90px;width:60px">A Title About Contents</div>
  <div class="dot" style="left:16px;top:142px"></div><div class="h" style="left:26px;top:140px;width:60px">A Title About Contents</div>
  <div class="red-bg" style="left:100px;top:44px;width:220px;height:4px"></div><div style="left:100px;top:52px;width:270px;height:3px;background:var(--mid)"></div>
  <div class="red-bg" style="left:100px;top:94px;width:180px;height:4px"></div><div style="left:100px;top:102px;width:270px;height:3px;background:var(--mid)"></div>
  <div class="red-bg" style="left:100px;top:144px;width:250px;height:4px"></div><div style="left:100px;top:152px;width:270px;height:3px;background:var(--mid)"></div>
  <div class="foot">© Copyright QTVlink. All rights reserved.</div>
</section>

<!-- 43 pie -->
<section class="slide">
  <div class="hd">Bullet &amp; Chart Area</div><div class="brand top">QTVlink</div>
  <svg style="left:30px;top:40px" width="120" height="120" viewBox="-60 -60 120 120"><path d="M0 0 0-50A50 50 0 1 1-29.4 40.5Z" fill="#e31f26"/><path d="M0 0-29.4 40.5A50 50 0 0 1-47.6-15.5Z" fill="#b9bdc6"/><path d="M0 0-47.6-15.5A50 50 0 0 1 0-50Z" fill="#4b5263"/></svg>
  <div class="h" style="left:12px;top:60px">15%</div><div class="h" style="left:10px;top:120px">25%</div><div class="h" style="left:156px;top:110px">60%</div>
  <div class="ico" style="left:200px;top:40px"></div><div class="h" style="left:218px;top:40px">Category One</div><div class="p" style="left:218px;top:49px">Lorem ipsum dolor sit.</div>
  <div class="ico s" style="left:200px;top:70px"></div><div class="h" style="left:218px;top:70px">Category Two</div><div class="p" style="left:218px;top:79px">Lorem ipsum dolor sit.</div>
  <div class="ico" style="left:200px;top:100px"></div><div class="h" style="left:218px;top:100px">Category Three</div><div class="p" style="left:218px;top:109px">Lorem ipsum dolor sit.</div>
  <div class="ico s" style="left:200px;top:130px"></div><div class="h" style="left:218px;top:130px">Category Four</div><div class="p" style="left:218px;top:139px">Lorem ipsum dolor sit.</div>
  <div class="foot">© Copyright QTVlink. All rights reserved.</div>
</section>

<!-- 44 timeline 2 -->
<section class="slide">
  <div style="left:90px;top:0;width:2px;height:222px;background:var(--red)"></div>
  <div class="dot" style="left:88px;top:20px;width:6px;height:6px"></div><div class="dot" style="left:88px;top:70px;width:6px;height:6px"></div><div class="dot" style="left:88px;top:130px;width:6px;height:6px"></div>
  <div class="h red" style="left:104px;top:18px;font-size:8px">Your<br>Title Here</div>
  <div class="h red" style="left:30px;top:66px;width:50px;text-align:right">Timeline<br>Point</div>
  <div class="pct" style="left:104px;top:64px">50%</div>
  <div class="p" style="left:104px;top:84px;width:200px">Lorem ipsum dolor sit amet, consectetur adipiscing elit.</div>
  <div class="h red" style="left:104px;top:128px">Your Title</div>
  <div class="p" style="left:104px;top:138px;width:200px">Lorem ipsum dolor sit amet, consectetur adipiscing elit sed do.</div>
</section>

<!-- 45 horizontal bars -->
<section class="slide">
  <div class="hd">Bullet &amp; Chart Area</div><div class="brand top">QTVlink</div>
  <svg style="left:20px;top:40px" width="170" height="120" viewBox="0 0 170 120"><g fill="#4b5263"><rect y="0" width="110" height="8"/><rect y="30" width="140" height="8"/><rect y="60" width="90" height="8"/><rect y="90" width="120" height="8"/></g><g fill="#e31f26"><rect y="10" width="70" height="8"/><rect y="40" width="100" height="8"/><rect y="70" width="150" height="8"/><rect y="100" width="60" height="8"/></g></svg>
  <div class="ico" style="left:220px;top:40px"></div><div class="h" style="left:238px;top:40px">Category One</div><div class="p" style="left:238px;top:49px">Lorem ipsum dolor sit.</div>
  <div class="ico s" style="left:220px;top:70px"></div><div class="h" style="left:238px;top:70px">Category Two</div><div class="p" style="left:238px;top:79px">Lorem ipsum dolor sit.</div>
  <div class="ico" style="left:220px;top:100px"></div><div class="h" style="left:238px;top:100px">Category Three</div><div class="p" style="left:238px;top:109px">Lorem ipsum dolor sit.</div>
  <div class="ico s" style="left:220px;top:130px"></div><div class="h" style="left:238px;top:130px">Category Four</div><div class="p" style="left:238px;top:139px">Lorem ipsum dolor sit.</div>
  <div class="foot">© Copyright QTVlink. All rights reserved.</div>
</section>

<!-- 46 bar chart bullets -->
<section class="slide">
  <div class="hd">Bullet &amp; Chart Area</div><div class="brand top">QTVlink</div>
  <div class="ico" style="left:14px;top:40px"></div><div class="h" style="left:32px;top:43px">Your Text Here</div>
  <div class="ico s" style="left:14px;top:66px"></div><div class="h" style="left:32px;top:69px">Your Text Here</div>
  <div class="ico" style="left:14px;top:92px"></div><div class="h" style="left:32px;top:95px">Your Text Here</div>
  <div class="ico s" style="left:14px;top:118px"></div><div class="h" style="left:32px;top:121px">Your Text Here</div>
  <div class="ico" style="left:14px;top:144px"></div><div class="h" style="left:32px;top:147px">Your Text Here</div>
  <svg style="left:170px;top:40px" width="200" height="120" viewBox="0 0 200 120"><g fill="#e31f26"><rect x="0" y="30" width="14" height="90"/><rect x="60" y="10" width="14" height="110"/><rect x="120" y="50" width="14" height="70"/></g><g fill="#4b5263"><rect x="16" y="60" width="14" height="60"/><rect x="76" y="40" width="14" height="80"/><rect x="136" y="20" width="14" height="100"/></g><line x1="0" y1="120" x2="200" y2="120" stroke="#b9bdc6"/></svg>
  <div class="foot">© Copyright QTVlink. All rights reserved.</div>
</section>

<!-- 47 column chart -->
<section class="slide">
  <div class="hd">Column Chart</div><div class="brand top">QTVlink</div>
  <svg style="left:20px;top:36px" width="350" height="110" viewBox="0 0 350 110"><g fill="#e31f26"><rect x="10" y="10" width="26" height="100"/><rect x="130" y="30" width="26" height="80"/><rect x="250" y="0" width="26" height="110"/></g><g fill="#4b5263"><rect x="40" y="40" width="26" height="70"/><rect x="160" y="20" width="26" height="90"/><rect x="280" y="50" width="26" height="60"/></g><g fill="#b9bdc6"><rect x="70" y="60" width="20" height="50"/><rect x="190" y="70" width="20" height="40"/><rect x="310" y="40" width="20" height="70"/></g></svg>
  <div class="p" style="left:24px;top:156px;width:100px">Lorem ipsum dolor sit amet.</div><div class="p" style="left:144px;top:156px;width:100px">Lorem ipsum dolor sit amet.</div><div class="p" style="left:264px;top:156px;width:100px">Lorem ipsum dolor sit amet.</div>
  <div class="foot">© Copyright QTVlink. All rights reserved.</div>
</section>

<!-- 48 three steps -->
<section class="slide">
  <div class="hd">Three Steps</div><div class="brand top">QTVlink</div>
  <div class="ico" style="left:14px;top:44px"></div><div class="h" style="left:32px;top:44px">Step One</div><div class="p" style="left:32px;top:53px">Lorem ipsum dolor sit amet.</div>
  <div class="ico s" style="left:14px;top:84px"></div><div class="h" style="left:32px;top:84px">Step Two</div><div class="p" style="left:32px;top:93px">Lorem ipsum dolor sit amet.</div>
  <div class="ico" style="left:14px;top:124px"></div><div class="h" style="left:32px;top:124px">Step Three</div><div class="p" style="left:32px;top:133px">Lorem ipsum dolor sit amet.</div>
  <svg style="left:230px;top:30px" width="150" height="150" viewBox="0 0 150 150"><circle cx="100" cy="40" r="26" fill="none" stroke="#e31f26" stroke-width="12"/><circle cx="60" cy="80" r="26" fill="none" stroke="#4b5263" stroke-width="12"/><circle cx="100" cy="115" r="26" fill="none" stroke="#e31f26" stroke-width="12"/><g font-family="Raleway" font-weight="700" font-size="8" text-anchor="middle"><text x="100" y="43" fill="#e31f26">abc</text><text x="60" y="83" fill="#4b5263">abc</text><text x="100" y="118" fill="#e31f26">abc</text></g></svg>
  <div class="foot">© Copyright QTVlink. All rights reserved.</div>
</section>

<!-- 49 project timeline -->
<section class="slide">
  <div class="hd">Project Timeline</div><div class="brand top">QTVlink</div>
  <svg style="left:14px;top:30px" width="362" height="150" viewBox="0 0 362 150"><rect width="362" height="12" fill="#4b5263"/><g stroke="#e3e5e9"><line x1="0" y1="30" x2="362" y2="30"/><line x1="0" y1="50" x2="362" y2="50"/><line x1="0" y1="70" x2="362" y2="70"/><line x1="0" y1="90" x2="362" y2="90"/><line x1="0" y1="110" x2="362" y2="110"/><line x1="0" y1="130" x2="362" y2="130"/></g><g font-family="Open Sans" font-size="5" fill="#fff"><text x="6" y="8">Task</text><text x="90" y="8">Jan</text><text x="150" y="8">Feb</text><text x="210" y="8">Mar</text><text x="270" y="8">Apr</text><text x="330" y="8">May</text></g><g font-family="Open Sans" font-size="5" fill="#8a8f9b"><text x="6" y="24">Research</text><text x="6" y="44">Planning</text><text x="6" y="64">Design</text><text x="6" y="84">Build</text><text x="6" y="104">Testing</text><text x="6" y="124">Launch</text></g><g fill="#e31f26"><rect x="80" y="17" width="70" height="8"/><rect x="190" y="57" width="90" height="8"/><rect x="280" y="117" width="70" height="8"/></g><g fill="#4b5263"><rect x="130" y="37" width="70" height="8"/><rect x="230" y="77" width="80" height="8"/><rect x="260" y="97" width="60" height="8"/></g></svg>
  <div class="dot" style="left:20px;top:190px"></div><div class="p" style="left:28px;top:188px">Phase one</div>
  <div class="dot" style="left:80px;top:190px;background:var(--slate)"></div><div class="p" style="left:88px;top:188px">Phase two</div>
  <div class="foot">© Copyright QTVlink. All rights reserved.</div>
</section>

<!-- 50 three bullets -->
<section class="slide">
  <div class="hd">Three Bullets Area</div><div class="brand top">QTVlink</div>
  <div class="ph blue" role="img" aria-label="Glowing city skyline" style="left:0;top:28px;right:0;height:110px"></div>
  <div class="ico" style="left:60px;top:70px;width:26px;height:26px"></div>
  <div class="ico s" style="left:182px;top:70px;width:26px;height:26px"></div>
  <div class="ico s" style="left:304px;top:70px;width:26px;height:26px"></div>
  <div class="p" style="left:24px;top:150px;width:100px;text-align:center">Lorem ipsum dolor sit amet, consectetur elit.</div>
  <div class="p" style="left:146px;top:150px;width:100px;text-align:center">Lorem ipsum dolor sit amet, consectetur elit.</div>
  <div class="p" style="left:268px;top:150px;width:100px;text-align:center">Lorem ipsum dolor sit amet, consectetur elit.</div>
  <div class="foot">© Copyright QTVlink. All rights reserved.</div>
</section>

<!-- 51 thank you -->
<section class="slide">
  <div class="ph dark" role="img" aria-label="Dark city towers" style="inset:0"></div>
  <div class="big" style="left:20px;top:40px;color:var(--red)">Thank <span style="color:#fff">You</span></div>
  <div class="p w" style="left:20px;top:62px">Your Subtitle Goes Here</div>
  <div class="brand lg" style="left:250px;top:60px;color:#fff">QTVlink</div>
  <div class="p w" style="left:20px;top:140px;line-height:10px">+1 555 010 2048<br>hello@qtvlink.com<br>www.qtvlink.com<br>200 Market Street, Suite 5</div>
</section>

</main>
</body>
</html>
```